I'd like a business card that makes my company, Fenwright Marsh Associates Ltd stand out from the normal financial & IT services sector . It would be great to have a card that a potential client will think "wow" this is out of the norm , I'll give these guys a call. My business aims to provide consultancy services for financial and IT institutions but I'm looking to provide a newer approach that fits into today's social media rather than the standard "big 4" approach. My business helps companies assess their internal issues and aims to solve issues via business process re-engineering. The final design should have a balance of the maturity of the financial & IT sector with the fresh approach of the thriving social media sector

Target Market(s)

Business Managers and Directors, technical Managers and directors. Aged between 20 and 60 that handle project budgets

Industry/Entity Type

Financial

Requirements
Must have
• Must incorporate company logo currently being designed
Should not have
• No old-style fonts please.

```html
<!DOCTYPE html>
<html lang="en">
<head>
<meta charset="utf-8">
<title>Fenwright Marsh Associates Ltd — Business Card</title>
<link rel="stylesheet" href="https://fonts.googleapis.com/css2?family=Open+Sans:wght@400;600;700;800&display=swap">
<style>
  :root {
    --backdrop: #2f2925;
    --paper: #ffffff;
    --ink: #111111;
    --card-black: #141414;
    --foil: #8d8d8d;
    --foil-dim: #6a6a6a;
  }
  * { box-sizing: border-box; margin: 0; padding: 0; }
  html, body { width: 1200px; height: 716px; overflow: hidden; }
  body {
    background: var(--backdrop);
    font-family: "Open Sans", Arial, sans-serif;
    position: relative;
  }
  .card {
    position: absolute;
    top: 198px;
    width: 540px;
    height: 320px;
    border-radius: 4px;
    overflow: hidden;
    box-shadow: 0 10px 30px rgba(0,0,0,.45);
  }
  .card-front { left: 50px; background: var(--paper); color: var(--ink); }
  .card-back { left: 610px; background: var(--card-black); }

  /* front */
  .brand {
    position: absolute;
    top: 30px;
    left: 190px;
    width: 230px;
    text-align: center;
  }
  .brand-mark {
    display: block;
    width: 46px;
    height: 46px;
    margin: 0 auto 8px;
    background: var(--ink);
  }
  .brand-name {
    font-weight: 800;
    font-size: 15px;
    line-height: 1.2;
    letter-spacing: .3px;
    color: var(--ink);
  }
  .band {
    position: absolute;
    top: 118px;
    left: 0;
    width: 540px;
    height: 42px;
    background: var(--ink);
  }
  .band-block {
    position: absolute;
    top: 118px;
    left: 400px;
    width: 140px;
    height: 104px;
    background: var(--ink);
  }
  .band-square {
    position: absolute;
    top: 168px;
    left: 440px;
    width: 40px;
    height: 40px;
    background: var(--paper);
  }
  .holder {
    position: absolute;
    top: 126px;
    left: 175px;
    color: var(--paper);
    display: flex;
    align-items: baseline;
    gap: 8px;
  }
  .holder-name { font-weight: 700; font-size: 18px; }
  .holder-role { font-size: 11px; border-left: 1px solid var(--paper); padding-left: 8px; }
  .contacts {
    position: absolute;
    top: 178px;
    left: 22px;
    list-style: none;
    font-size: 13px;
    font-weight: 600;
    line-height: 22px;
  }
  .contacts li { display: flex; align-items: center; gap: 9px; }
  .contact-icon {
    width: 14px; height: 14px;
    background: var(--ink);
    border-radius: 2px;
    display: inline-flex; align-items: center; justify-content: center;
  }
  .address {
    position: absolute;
    top: 234px;
    left: 340px;
    width: 190px;
    font-size: 13px;
    font-weight: 700;
    line-height: 17px;
  }

  /* back */
  .back-brand {
    position: absolute;
    top: 105px;
    left: 0;
    width: 540px;
    text-align: center;
  }
  .back-mark {
    display: block;
    width: 64px; height: 64px;
    margin: 0 auto 12px;
    background: var(--foil-dim);
  }
  .back-name {
    font-weight: 800;
    font-size: 22px;
    line-height: 1.25;
    letter-spacing: .5px;
    color: var(--foil);
  }
</style>
</head>
<body>
  <section class="card card-front" aria-label="Business card front">
    <div class="brand">
      <span class="brand-mark"></span>
      <p class="brand-name">FENWRIGHT MARSH<br>Associates Ltd</p>
    </div>
    <div class="band"></div>
    <div class="band-block"></div>
    <div class="band-square"></div>
    <div class="holder">
      <span class="holder-name">Daniel Hartley</span>
      <span class="holder-role">Director</span>
    </div>
    <ul class="contacts">
      <li><span class="contact-icon"><svg width="9" height="9" viewBox="0 0 10 10"><path d="M2 1l2 2-1 1.3a6 6 0 0 0 2.7 2.7L7 6l2 2-1.3 1.3C4.5 9 1 5.5.7 2.3z" fill="#fff"/></svg></span>647-318-262</li>
      <li><span class="contact-icon"><svg width="9" height="9" viewBox="0 0 10 10"><path d="M2 1l2 2-1 1.3a6 6 0 0 0 2.7 2.7L7 6l2 2-1.3 1.3C4.5 9 1 5.5.7 2.3z" fill="#fff"/></svg></span>647-406-719</li>
      <li><span class="contact-icon"><svg width="9" height="9" viewBox="0 0 10 10"><circle cx="5" cy="5" r="4" fill="none" stroke="#fff"/><path d="M1 5h8M5 1c-2 2.5-2 5.5 0 8M5 1c2 2.5 2 5.5 0 8" fill="none" stroke="#fff" stroke-width=".8"/></svg></span>www.fenwrightmarsh.com</li>
      <li><span class="contact-icon"><svg width="9" height="9" viewBox="0 0 10 10"><rect x="1" y="2.5" width="8" height="5.5" fill="none" stroke="#fff"/><path d="M1 2.5l4 3 4-3" fill="none" stroke="#fff"/></svg></span>info@fenwrightmarsh.com</li>
    </ul>
    <p class="address">24 Carver Street West,<br>Ground Floor,<br>Brookfield,<br>ON L8P 2K5</p>
  </section>

  <section class="card card-back" aria-label="Business card back">
    <div class="back-brand">
      <span class="back-mark"></span>
      <p class="back-name">FENWRIGHT MARSH<br>Associates Ltd</p>
    </div>
  </section>
</body>
</html>
```